Calloway needs a modernized design

We would like a modern update (that can be responsive) to our existing website. Attached are the two existing pages we would like new concepts of - our home page and a page about one of our locations.

Calloway is provides executive offices and virtual office services. Startups, law firms, and financial services are our primary clients. We would like a professional, clean design, leaning towards minimalist. We intend to greatly reduce/eliminate the long paragraphs of text.

Industry/Entity Type

Business Service

Number of Pages Required

2 page

Requirements
Must have
• A design that can be responsive
Nice to have
• Large image(s) on home page that rotate.

```html
<!DOCTYPE html>
<html lang="en">
<head>
<meta charset="utf-8">
<title>Calloway Business Centers</title>
<link href="https://fonts.googleapis.com/css2?family=Bitter:wght@400;700&family=Open+Sans:wght@400;600;700&display=swap" rel="stylesheet">
<style>
:root{
  --navy:#25366b;
  --navy-dark:#1d2b58;
  --ink:#222;
  --muted:#444;
  --grey-band:#ececec;
  --ring:#d9d9d9;
  --icon-grey:#6b6b6b;
  --link-blue:#3f88d6;
  --footer:#2b3a6e;
  --footer-bar:#151515;
  --white:#fff;
}
*{margin:0;padding:0;box-sizing:border-box}
html,body{width:1200px;height:2853px;overflow:hidden;background:var(--white)}
body{position:relative;font-family:"Open Sans",Arial,sans-serif;color:var(--ink)}
.abs{position:absolute}
.serif{font-family:"Bitter",Georgia,serif}

/* header */
.brand{left:48px;top:15px;display:flex;align-items:center;gap:12px}
.brand-mark{width:74px;height:74px;border-radius:50%;background:var(--navy)}
.brand-name{font-family:"Bitter",Georgia,serif;color:var(--navy);font-size:30px;font-weight:700;line-height:1}
.brand-sub{font-family:"Bitter",Georgia,serif;color:var(--navy);font-size:15px;letter-spacing:1px;margin-top:6px}
.phones{right:48px;top:8px;font-family:"Bitter",Georgia,serif;font-size:25px;color:var(--navy)}
.nav{left:420px;top:57px;display:flex;height:50px;font-family:"Bitter",Georgia,serif;font-size:14px;letter-spacing:.5px}
.nav a{display:flex;align-items:center;padding:0 30px;color:var(--ink);text-decoration:none}
.nav a.active{background:var(--navy);color:var(--white);padding:0 26px;width:100px;justify-content:center}
.nav-rule{left:48px;top:105px;width:1104px;height:4px;background:var(--navy-dark)}

/* hero */
.hero{left:0;top:122px;width:1200px;height:525px;background:linear-gradient(100deg,#e9edf2 0%,#c5ccd6 40%,#5c6e8a 70%,#2c3a55 100%)}
.hero-panel{left:49px;top:228px;width:500px;height:305px;background:rgba(255,255,255,.72);padding:30px 30px}
.hero-kicker{font-family:"Bitter",Georgia,serif;font-size:34px;color:#333;letter-spacing:1px}
.hero-title{font-family:"Open Sans",Arial,sans-serif;font-size:48px;font-weight:700;color:#222;line-height:1.1}
.hero-copy{font-size:14px;line-height:1.6;color:#222;margin-top:14px;width:450px}
.btn{display:inline-flex;align-items:center;justify-content:center;border:2px solid #333;font-size:13px;color:#222;background:transparent}
.hero .btn,.hero-panel .btn{margin-top:18px;width:118px;height:41px}

/* services */
.service{width:200px;text-align:center}
.service-ring{width:172px;height:172px;border-radius:50%;background:var(--ring);margin:0 auto;display:flex;align-items:center;justify-content:center}
.service-inner{width:144px;height:144px;border-radius:50%;background:var(--navy);display:flex;align-items:center;justify-content:center}
.service-core{width:104px;height:104px;border-radius:50%;background:var(--icon-grey);display:flex;align-items:center;justify-content:center}
.service-label{font-family:"Bitter",Georgia,serif;font-weight:700;font-size:19px;line-height:1.15;margin-top:20px;color:#222}
.service-bar{width:56px;height:4px;background:#666;margin:8px auto 0}
.service-bar.on{background:var(--navy)}

/* features band */
.band{left:0;top:989px;width:1200px;height:612px;background:var(--grey-band)}
.band-heading{left:60px;top:1020px;width:1080px;text-align:center;font-family:"Bitter",Georgia,serif;font-size:23px;line-height:1.3;color:var(--navy)}
.feature{width:340px;text-align:center}
.feature-photo{width:228px;height:228px;border-radius:50%;border:6px solid var(--white);margin:0 auto}
.feature-title{font-family:"Bitter",Georgia,serif;font-weight:700;font-size:25px;color:var(--navy);margin-top:22px}
.feature-copy{font-size:13px;line-height:1.6;color:#333;margin-top:10px;height:92px}
.feature .btn{width:98px;height:34px;font-size:12px;border:1px solid #777;margin-top:14px}

/* videos and news */
.section-title{font-family:"Bitter",Georgia,serif;font-size:34px;color:#222}
.video{width:284px}
.video-thumb{width:284px;height:182px;background:linear-gradient(135deg,#6a5040,#a88a70 45%,#4a3a34);position:relative}
.play{position:absolute;left:120px;top:70px}
.video-title{font-size:15px;font-weight:700;margin-top:18px}
.video-copy{font-size:14px;line-height:1.5;color:#333;margin-top:8px}
.video-meta{font-size:13px;color:#333;margin-top:12px;display:flex;align-items:center;gap:6px}
.divider{left:704px;top:1674px;width:1px;height:400px;background:#cfcfcf}
.news{display:flex;gap:20px;width:420px}
.news-date{width:92px;height:92px;border-radius:50%;border:4px solid var(--navy);flex:none;display:flex;align-items:center;justify-content:center}
.news-date span{width:70px;height:70px;border-radius:50%;background:var(--navy);color:var(--white);font-weight:700;font-size:16px;display:flex;flex-direction:column;align-items:center;justify-content:center;line-height:1.2}
.news-title{font-size:15px;font-weight:700;line-height:1.3;margin-top:4px}
.news-copy{font-size:16px;line-height:1.45;color:#444}

/* experts */
.experts{left:0;top:2134px;width:1200px;height:424px;background:linear-gradient(90deg,#3d3d3d,#555 50%,#2f2f2f)}
.experts-title{left:0;top:2180px;width:1200px;text-align:center;font-family:"Bitter",Georgia,serif;font-size:36px;color:var(--white)}
.quote{left:140px;top:2252px;width:920px;text-align:center;color:var(--white);font-size:15px;line-height:1.65}
.cite{left:0;top:2380px;width:1200px;text-align:center;color:var(--link-blue);font-size:15px}
.dots{left:542px;top:2430px;display:flex;gap:8px}
.dots i{display:block;width:34px;height:6px;background:#ddd}
.dots i.on{background:var(--link-blue)}
.experts-btn{left:517px;top:2467px;width:153px;height:44px;border:2px solid var(--white);color:var(--white);font-size:13px}

/* footer */
.footer{left:0;top:2558px;width:1200px;height:244px;background:var(--footer);color:var(--white)}
.footer h3{font-family:"Open Sans",Arial,sans-serif;font-weight:400;font-size:23px}
.foot-links{display:grid;grid-template-columns:199px 150px;row-gap:7px;font-size:15px;margin-top:22px}
.news-sub{font-size:17px;color:#cfd6ea;margin-top:12px}
.news-copy-foot{font-size:13px;line-height:1.6;margin-top:14px;width:270px}
.subscribe{display:flex;margin-top:24px}
.subscribe .field{width:172px;height:33px;background:var(--white);color:#888;font-size:12px;padding:8px 8px}
.subscribe .go{width:81px;height:33px;background:#e8e8e8;color:#999;font-size:12px;display:flex;align-items:center;justify-content:center}
.social{display:flex;gap:8px;margin-top:22px}
.social i{display:block;width:38px;height:38px;border-radius:50%}
.foot-brand{display:flex;align-items:center;gap:10px;margin-top:24px}
.foot-brand .mark{width:56px;height:56px;border-radius:50%;background:#d8d4c8}
.foot-brand .name{font-family:"Bitter",Georgia,serif;font-size:24px;font-weight:700;color:var(--white)}
.copyright{left:0;top:2802px;width:1200px;height:51px;background:var(--footer-bar);color:var(--white);font-size:12px;display:flex;align-items:center;justify-content:center;letter-spacing:.3px}
</style>
</head>
<body>

<header>
  <div class="abs brand">
    <div class="brand-mark"></div>
    <div>
      <div class="brand-name">CALLOWAY</div>
      <div class="brand-sub">BUSINESS CENTERS</div>
    </div>
  </div>
  <div class="abs phones">Dallas 214.555.0142 | Houston 713.555.0187</div>
  <nav class="abs nav">
    <a class="active">HOME</a>
    <a>PROPERTIES</a>
    <a>VIRTUAL TOURS &amp; VIDEOS</a>
    <a>PHOTOS</a>
    <a>BROKER REFERRALS</a>
  </nav>
  <div class="abs nav-rule"></div>
</header>

<section class="abs hero" role="img" aria-label="Business people reviewing documents with a pen at a desk"></section>
<div class="abs hero-panel">
  <div class="hero-kicker">EXECUTIVE OFFICE SUITES</div>
  <div class="hero-title">ON LOW COST</div>
  <p class="hero-copy">Your company works hard to generate new business and stay competitive, so understanding how your products fare in the market, understanding customer buying habits, or even understanding where your sales force is failing, can give you the edge you need.</p>
  <span class="btn">READ MORE</span>
</div>

<section class="services">
  <div class="abs service" style="left:33px;top:684px">
    <div class="service-ring"><div class="service-inner"><div class="service-core">
      <svg width="44" height="48" viewBox="0 0 44 48"><circle cx="22" cy="13" r="10" fill="#fff"/><path d="M2 48 Q2 28 22 28 Q42 28 42 48Z" fill="#fff"/><path d="M20 28 L24 28 L23 42 L21 42Z" fill="#6b6b6b"/></svg>
    </div></div></div>
    <div class="service-label">Executive Office<br>Suites</div>
    <div class="service-bar on"></div>
  </div>
  <div class="abs service" style="left:263px;top:684px">
    <div class="service-ring"><div class="service-inner"><div class="service-core">
      <svg width="56" height="44" viewBox="0 0 56 44"><circle cx="28" cy="9" r="8" fill="#fff"/><circle cx="10" cy="13" r="6" fill="#fff"/><circle cx="46" cy="13" r="6" fill="#fff"/><rect x="20" y="19" width="16" height="25" rx="3" fill="#fff"/><rect x="4" y="21" width="12" height="20" rx="3" fill="#fff"/><rect x="40" y="21" width="12" height="20" rx="3" fill="#fff"/></svg>
    </div></div></div>
    <div class="service-label">On-demand<br>Meeting Rooms</div>
    <div class="service-bar"></div>
  </div>
  <div class="abs service" style="left:501px;top:684px">
    <div class="service-ring"><div class="service-inner"><div class="service-core">
      <svg width="54" height="48" viewBox="0 0 54 48"><rect x="4" y="2" width="46" height="30" fill="none" stroke="#fff" stroke-width="3"/><rect x="24" y="10" width="14" height="12" fill="#fff"/><circle cx="14" cy="16" r="4" fill="#fff"/><circle cx="10" cy="40" r="4" fill="#fff"/><circle cx="27" cy="40" r="4" fill="#fff"/><circle cx="44" cy="40" r="4" fill="#fff"/></svg>
    </div></div></div>
    <div class="service-label">On-demand<br>Training Rooms</div>
    <div class="service-bar"></div>
  </div>
  <div class="abs service" style="left:731px;top:684px">
    <div class="service-ring"><div class="service-inner"><div class="service-core">
      <svg width="50" height="48" viewBox="0 0 50 48"><circle cx="16" cy="20" r="7" fill="#fff"/><path d="M2 44 Q2 30 16 30 Q30 30 30 44Z" fill="#fff"/><rect x="32" y="2" width="14" height="24" rx="2" fill="none" stroke="#fff" stroke-width="3"/><rect x="36" y="8" width="6" height="10" fill="#fff"/></svg>
    </div></div></div>
    <div class="service-label">Virtual Office<br>Solutions</div>
    <div class="service-bar"></div>
  </div>
  <div class="abs service" style="left:965px;top:684px">
    <div class="service-ring"><div class="service-inner"><div class="service-core">
      <svg width="54" height="46" viewBox="0 0 54 46"><circle cx="18" cy="18" r="8" fill="#fff"/><path d="M4 44 Q4 30 18 30 Q32 30 32 44Z" fill="#fff"/><rect x="30" y="2" width="22" height="16" fill="none" stroke="#fff" stroke-width="3"/><circle cx="41" cy="10" r="3" fill="#fff"/></svg>
    </div></div></div>
    <div class="service-label">Video Conference<br>Solutions</div>
    <div class="service-bar"></div>
  </div>
</section>

<section class="abs band"></section>
<h2 class="abs band-heading">Come See Why Smarter Companies are Choosing Calloway Business Centers' Dallas, Ft. Worth and Houston Executive Office Suites, Virtual Offices, Meeting Rooms and Video Conferencing.</h2>

<div class="abs feature" style="left:45px;top:1126px">
  <div class="feature-photo" role="img" aria-label="Hand touching a glowing digital network display" style="background:radial-gradient(circle,#9fc4e6,#3d6a9a 60%,#1b3553)"></div>
  <div class="feature-title">Value</div>
  <p class="feature-copy">Either you need Dallas/Ft. Worth Office Space, Dallas Executive Suites, Ft. Worth Executive Suites, Houston Office Space, Houston Executive Suites, or maybe you simply need a place to stop in and use an on-demand</p>
  <span class="btn">READ MORE</span>
</div>
<div class="abs feature" style="left:431px;top:1126px">
  <div class="feature-photo" role="img" aria-label="Thoughtful woman surrounded by colourful lines of ideas" style="background:radial-gradient(circle,#b8a592,#6f655c 60%,#3f3a36)"></div>
  <div class="feature-title">Community</div>
  <p class="feature-copy">Companies that partner with Calloway share more than a prestigious address. They also share ideas and services. Our Executive Office Business Centers are places where savvy, growing companies</p>
  <span class="btn">READ MORE</span>
</div>
<div class="abs feature" style="left:806px;top:1126px">
  <div class="feature-photo" role="img" aria-label="Two colleagues working together at a laptop" style="background:radial-gradient(circle,#e9eef3,#a7b8cc 60%,#6f87a6)"></div>
  <div class="feature-title">Service</div>
  <p class="feature-copy">Calloway Business Centers positions its management team in every one of its business centers - we operate with an open-door policy as a medium-sized company without all of the corporate bureaucracy and red tape.</p>
  <span class="btn">READ MORE</span>
</div>

<h2 class="abs section-title" style="left:49px;top:1667px">Our Videos</h2>
<article class="abs video" style="left:49px;top:1737px">
  <div class="video-thumb" role="img" aria-label="Video still of a woman wearing a headset">
    <svg class="play" width="46" height="34" viewBox="0 0 46 34"><rect width="46" height="34" rx="9" fill="#d62020"/><path d="M18 10 L30 17 L18 24Z" fill="#fff"/></svg>
  </div>
  <div class="video-title">Learn the language of love</div>
  <p class="video-copy">Education is the process of facilitating learning. Knowledge, skills, values, beliefs, and habits of a...</p>
  <div class="video-meta">
    <svg width="18" height="18" viewBox="0 0 18 18"><circle cx="9" cy="10" r="7" fill="none" stroke="#222" stroke-width="2"/><path d="M9 6 V10 H12" stroke="#222" stroke-width="2" fill="none"/></svg>2015-07-13
    <svg width="18" height="16" viewBox="0 0 18 16" style="margin-left:10px"><path d="M9 2 C4 2 1 4.5 1 7.5 C1 9.5 2.5 11 4 12 L3 15 L7 13 C7.6 13 8.3 13 9 13 C14 13 17 10.5 17 7.5 C17 4.5 14 2 9 2Z" fill="none" stroke="#222" stroke-width="1.5"/></svg>(4) by marlow
  </div>
</article>
<article class="abs video" style="left:375px;top:1737px">
  <div class="video-thumb" role="img" aria-label="Video still of a woman wearing a headset">
    <svg class="play" width="46" height="34" viewBox="0 0 46 34"><rect width="46" height="34" rx="9" fill="#d62020"/><path d="M18 10 L30 17 L18 24Z" fill="#fff"/></svg>
  </div>
  <div class="video-title">Learn the language of love</div>
  <p class="video-copy">Education is the process of facilitating learning. Knowledge, skills, values, beliefs, and habits of a...</p>
  <div class="video-meta">
    <svg width="18" height="18" viewBox="0 0 18 18"><circle cx="9" cy="10" r="7" fill="none" stroke="#222" stroke-width="2"/><path d="M9 6 V10 H12" stroke="#222" stroke-width="2" fill="none"/></svg>2015-07-13
    <svg width="18" height="16" viewBox="0 0 18 16" style="margin-left:10px"><path d="M9 2 C4 2 1 4.5 1 7.5 C1 9.5 2.5 11 4 12 L3 15 L7 13 C7.6 13 8.3 13 9 13 C14 13 17 10.5 17 7.5 C17 4.5 14 2 9 2Z" fill="none" stroke="#222" stroke-width="1.5"/></svg>(4) by marlow
  </div>
</article>

<div class="abs divider"></div>
<h2 class="abs section-title" style="left:746px;top:1656px">Our News</h2>
<article class="abs news" style="left:734px;top:1734px">
  <div class="news-date"><span>Nov<br>01</span></div>
  <div><div class="news-title">The Surprising Reason College Expensive</div><p class="news-copy">Cras condimentum a elit eget sagittis. Ut dignissim sapien feugiat...</p></div>
</article>
<article class="abs news" style="left:734px;top:1846px">
  <div class="news-date"><span>Nov<br>21</span></div>
  <div><div class="news-title">The Surprising Reason College Expensive</div><p class="news-copy">Cras condimentum a elit eget sagittis. Ut dignissim sapien feugiat...</p></div>
</article>
<article class="abs news" style="left:734px;top:1958px">
  <div class="news-date"><span>Nov<br>11</span></div>
  <div><div class="news-title">The Surprising Reason College Expensive</div><p class="news-copy">Cras condimentum a elit eget sagittis. Ut dignissim sapien feugiat...</p></div>
</article>

<section class="abs experts" role="img" aria-label="Businessman in a suit, darkened background"></section>
<h2 class="abs experts-title">Ask Our Experts</h2>
<blockquote class="abs quote">"Brightline Software's reputation for extensive knowledge of business intelligence analytics has a well-founded basis. Partnering with them was a win-win from day one onward, repeatedly demonstrated by our teams working together in unified fashion to quickly identify and resolve technical issues while delivering highly valued solutions that solved difficult market problems. A solid talented group of professionals who are a pleasure to engage with."</blockquote>
<div class="abs cite">Dr. Alan Whitcombe, Vice President/General Manager - Analytics, Leading Healthcare IT Company</div>
<div class="abs dots"><i class="on"></i><i></i><i></i></div>
<span class="abs btn experts-btn">READ MORE</span>

<footer class="abs footer">
  <div class="abs" style="left:86px;top:40px">
    <h3>Navigation Links</h3>
    <div class="foot-links">
      <span>About Us</span><span>Careers</span>
      <span>Contact Us</span><span>Furniture</span>
      <span>Forms</span><span>Specials</span>
      <span>Testimonials</span><span>Site Map</span>
      <span>FAQs</span><span>Privacy</span>
    </div>
  </div>
  <div class="abs" style="left:495px;top:40px">
    <h3>Newsletter Letter</h3>
    <div class="news-sub">Sign up to our mailing list</div>
    <p class="news-copy-foot">Suspendisse tempus sodales neque, eget eleifend turpis tristique eu.</p>
    <div class="subscribe"><div class="field">Email</div><div class="go">Subscribe</div></div>
  </div>
  <div class="abs" style="left:879px;top:40px">
    <h3>Social Media</h3>
    <div class="social">
      <i style="background:#3b5998"></i><i style="background:#1da1f2"></i><i style="background:#cc2020"></i><i style="background:#517fa4"></i><i style="background:#dd4b39"></i>
    </div>
    <div class="foot-brand"><div class="mark"></div><div class="name">CALLOWAY</div></div>
  </div>
</footer>
<div class="abs copyright">COPYRIGHT 2012 CALLOWAY BUSINESS CENTERS ALL RIGHTS RESERVED</div>

</body>
</html>
```